Harborlight Willow Home Care Business Cards

We are looking to create double sided, sleek business cards for our new Home Health Care Agency, Harborlight Willow Home Care, located in NJ. We want to appear established, professional and at the same time, stand out with a creative and original flair. It should have a luxurious, exclusive feel to it.
The theme colors from our logo should be incorporated into the project.

Our Logo is attached.

Information to be included on the business cards:

Insert Phone Icon: (555)-204-7390
Insert Website Icon: hwhcpx.example
Insert E-mail Icon: info@hwhcpx.example

Follow us on Social Media!
Insert Facebook Icon: (I will provide the link at a later time)
Insert Instagram Icon (I will provide the link at a later time)

In regard to location, we service the areas of: Bayville
Beachwood
Brick
Deal
Howell
Island Heights
Jackson
Lakehurst
Lakewood
Manchester Township
Point Pleasant Beach
Roosevelt
Long Branch
Toms River

All all it's neighboring areas.

However, that can take up a lot of room...therefore, I had in mind to use the backside of the card to have a MAP with all these areas marked on there...in addition to listing these service locations below the map.

We want the card to appear lively and vibrant.

Please note: I will provide the potential winner with the contact's name later on in the process.

A sample idea is attached below as well.

Use your creative juices!

Good luck!

• A map of our service areas on the back of the double sided card.
Sleek design
Our logo (refer to attachment below)

```html
<!DOCTYPE html>
<html lang="en">
<head>
<meta charset="utf-8">
<title>Harborlight Willow Home Care – Business Cards</title>
<link rel="stylesheet" href="https://fonts.googleapis.com/css2?family=Montserrat:wght@400;500;700&family=Roboto+Condensed:wght@400&display=swap">
<style>
  :root {
    --backdrop: #1f1f1f;
    --navy: #0d3f99;
    --navy-deep: #0a3587;
    --ink-blue: #163b8a;
    --green: #7dbb2f;
    --paper: #f3f3f2;
    --text-grey: #4a4a4a;
    --white: #ffffff;
  }
  * { margin: 0; padding: 0; box-sizing: border-box; }
  html, body {
    width: 1200px; height: 997px; overflow: hidden;
    background: var(--backdrop);
  }
  .canvas { position: relative; width: 1200px; height: 997px; }

  .card {
    position: absolute; left: 294px; width: 599px;
    box-shadow: 0 10px 24px rgba(0,0,0,0.55);
  }

  /* Back of card */
  .card-back {
    top: 146px; height: 340px;
    background: radial-gradient(ellipse at 50% 40%, #1149a8 0%, var(--navy) 55%, var(--navy-deep) 100%);
    color: var(--white);
    overflow: hidden;
  }
  .service-map {
    position: absolute; left: 0; top: 27px; width: 599px; height: 252px;
    background: radial-gradient(ellipse at 50% 50%, rgba(70,120,210,0.35) 0%, rgba(70,120,210,0.12) 60%, rgba(70,120,210,0) 80%);
  }
  .back-brand {
    position: absolute; left: 0; right: 0; top: 128px;
    display: flex; align-items: center; justify-content: center; gap: 10px;
    font-family: "Montserrat", sans-serif; font-weight: 700;
    font-size: 20px; color: var(--white); letter-spacing: 0.3px;
  }
  .brand-dot {
    width: 16px; height: 16px; border-radius: 50%; background: var(--green);
    flex: none;
  }
  .service-areas {
    position: absolute; left: 0; right: 0; top: 276px;
    text-align: center;
    font-family: "Roboto Condensed", sans-serif; font-size: 15px; line-height: 21px;
  }
  .service-areas .sep { color: var(--green); margin: 0 5px; }

  /* Front of card */
  .card-front {
    top: 522px; height: 342px;
    background: var(--paper);
    font-family: "Montserrat", sans-serif;
  }
  .front-brand {
    position: absolute; right: 26px; top: 72px;
    display: flex; align-items: center; gap: 8px;
    font-weight: 700; font-size: 16px; color: var(--ink-blue);
  }
  .holder { position: absolute; left: 25px; top: 176px; }
  .holder-name { font-weight: 700; font-size: 20px; color: var(--ink-blue); letter-spacing: 0.5px; }
  .holder-title { font-size: 15px; color: var(--text-grey); margin-top: 4px; }
  .rule {
    position: absolute; left: 25px; right: 26px; top: 236px;
    height: 1.5px; background: var(--ink-blue);
  }
  .contact-list, .social-list {
    position: absolute; list-style: none;
    font-size: 15.5px; color: var(--text-grey);
  }
  .contact-list { left: 25px; top: 255px; }
  .social-list { left: 353px; top: 256px; }
  .contact-list li, .social-list li {
    display: flex; align-items: center; gap: 7px; height: 21.5px;
  }
  .social-heading {
    font-weight: 700; font-size: 15px; color: var(--ink-blue); height: 24px !important;
  }
  .icon { width: 13px; height: 13px; flex: none; }
  .social-mark { width: 11px; height: 11px; background: var(--green); flex: none; margin-right: 2px; }
  .social-mark.round { border-radius: 50%; }
</style>
</head>
<body>
<div class="canvas">

  <section class="card card-back">
    <div class="service-map" role="img" aria-label="Dotted world map in light blue tones behind the brand"></div>
    <div class="back-brand"><span class="brand-dot"></span>Harborlight Willow Home Care</div>
    <p class="service-areas">
      Beachwood<span class="sep">•</span>Brick<span class="sep">•</span>Deal<span class="sep">•</span>Howell<span class="sep">•</span>Island Heights<span class="sep">•</span>Jackson<span class="sep">•</span>Lakehurst<span class="sep">•</span>Lakewood<br>
      Manchester Township<span class="sep">•</span>Point Pleasant Beach<span class="sep">•</span>Roosevelt<span class="sep">•</span>Long Branch<span class="sep">•</span>Toms River
    </p>
  </section>

  <section class="card card-front">
    <div class="front-brand"><span class="brand-dot"></span>Harborlight Willow Home Care</div>

    <div class="holder">
      <h1 class="holder-name">JORDAN AVERY</h1>
      <p class="holder-title">President</p>
    </div>

    <div class="rule"></div>

    <ul class="contact-list">
      <li>
        <svg class="icon" viewBox="0 0 24 24"><path fill="#7dbb2f" d="M6.6 10.8a15.1 15.1 0 0 0 6.6 6.6l2.2-2.2a1 1 0 0 1 1-.25 11.4 11.4 0 0 0 3.6.57 1 1 0 0 1 1 1V20a1 1 0 0 1-1 1A17 17 0 0 1 3 4a1 1 0 0 1 1-1h3.5a1 1 0 0 1 1 1c0 1.25.2 2.45.57 3.57a1 1 0 0 1-.25 1z"/></svg>
        (555)-204-7390
      </li>
      <li>
        <svg class="icon" viewBox="0 0 24 24"><path fill="#7dbb2f" d="M2 5h20v14H2z"/><path fill="none" stroke="#f3f3f2" stroke-width="1.8" d="M2 6l10 7 10-7"/></svg>
        info@hwhcpx.example
      </li>
      <li>
        <svg class="icon" viewBox="0 0 24 24"><circle cx="12" cy="12" r="10" fill="#7dbb2f"/><path fill="none" stroke="#f3f3f2" stroke-width="1.5" d="M2 12h20M12 2c3 3 3 17 0 20M12 2c-3 3-3 17 0 20"/></svg>
        www.hwhcpx.example
      </li>
    </ul>

    <ul class="social-list">
      <li class="social-heading">Follow us on Social Media!</li>
      <li><span class="social-mark"></span>/HarborlightWillow</li>
      <li><span class="social-mark round"></span>@HarborlightWillow</li>
    </ul>
  </section>

</div>
</body>
</html>
```